psd/html for a e wallet payment website designed

hi
i am in need of a psd / html for a whole website designed
the site is a e wallet /payment system i can i will provide a link to what type of style i am looking for but i can not stress this enough i do not want anyone replicating the website i am just providing the links to show you what kind of function and the content that is involved also, i have a srs with detailed pages you can read and refer to if need be
thanks of viewing
Vantoleaf.com
Brisklune.com
marblequivercoin.com
Qrdelivane.com

```html
<!DOCTYPE html>
<html lang="en">
<head>
<meta charset="utf-8">
<title>Paysora — Home</title>
<link href="https://fonts.googleapis.com/css2?family=Roboto:wght@400;500;700&family=Roboto+Condensed:wght@400;700&display=swap" rel="stylesheet">
<style>
:root{
  --blue:#29a7df;
  --blue-dark:#1b8fc4;
  --red:#e84340;
  --ink:#3c3c3c;
  --ink-soft:#666;
  --muted:#9a9a9a;
  --line:#e2e2e2;
  --bg:#f1f1f1;
  --panel:#ffffff;
  --topbar:#3a3a3a;
  --hero:#4a4a4a;
  --footer:#e6e6e6;
  --green:#5a9e2f;
}
*{box-sizing:border-box;margin:0;padding:0}
html,body{width:1200px;height:2492px;overflow:hidden}
body{font-family:"Roboto",Arial,sans-serif;color:var(--ink);background:var(--bg);position:relative}
a{color:inherit;text-decoration:none}
.abs{position:absolute}

/* top bar */
.topbar{left:0;top:0;width:1200px;height:33px;background:var(--topbar);color:#cfcfcf;font-size:13px}
.topbar .lang{position:absolute;top:0;height:33px;line-height:33px;width:40px;text-align:center}
.topbar .lang.active{background:#555;color:#fff}
.topbar .util{position:absolute;top:0;line-height:33px}

/* header */
.header{left:0;top:33px;width:1200px;height:113px;background:#fff;border-bottom:1px solid var(--line)}
.brand-name{position:absolute;left:42px;top:33px;font-size:40px;font-weight:400;color:var(--ink);letter-spacing:-.5px;line-height:48px}
.nav a{position:absolute;top:44px;font-size:17px;color:#444}
.nav .caret{font-size:11px;color:#999;margin-left:3px}
.nav-active-bar{left:487px;top:141px;width:97px;height:5px;background:var(--blue)}

/* hero */
.hero{left:0;top:146px;width:1200px;height:336px;background:linear-gradient(#3d3d3d,#555 50%,#3d3d3d)}
.hero-card{position:absolute;top:21px;height:295px;border-radius:4px;overflow:hidden;background:linear-gradient(#fdfdfd,#e9eaeb);box-shadow:0 2px 6px rgba(0,0,0,.4)}
.hero-card.users{left:42px;width:547px}
.hero-card.business{left:613px;width:545px}
.hero-photo{position:absolute;left:0;top:0;width:290px;height:295px;background:linear-gradient(135deg,#cfdde8,#e8d6c8 55%,#b9c9d8)}
.hero-illus{position:absolute;inset:0;background:linear-gradient(120deg,#eef2f5,#dfe7ee 45%,#d6e9c8 80%,#eef2f5)}
.counter{position:absolute;left:301px;top:45px;display:flex;gap:7px}
.counter span{width:32px;height:44px;border:1px solid #cfcfcf;border-radius:3px;background:linear-gradient(#fff,#ececec);font-size:30px;line-height:42px;text-align:center;color:#555}
.counter-label{position:absolute;left:301px;top:104px;width:190px;text-align:center;font-size:17px;color:#555;font-weight:500}
.counter-rule{position:absolute;left:301px;top:130px;width:190px;height:1px;background:#ccc}
.hero-btn{position:absolute;top:189px;width:203px;height:57px;line-height:57px;text-align:center;color:#fff;font-size:20px;font-weight:500;border-radius:3px}
.hero-btn.blue{left:296px;background:var(--blue)}
.hero-btn.red{left:46px;background:var(--red)}

/* section headings */
.sec-title{position:absolute;left:42px;width:736px;display:flex;align-items:center;gap:18px;font-family:"Roboto Condensed",sans-serif;font-weight:700;font-size:25px;color:#444;text-transform:uppercase}
.sec-title::before,.sec-title::after{content:"";flex:1;height:6px;background:repeating-linear-gradient(90deg,#ddd 0 2px,transparent 2px 4px)}

/* tabs + countries */
.tabs{left:42px;top:597px;width:736px;height:44px;border-bottom:3px solid var(--blue)}
.tab{position:absolute;top:0;width:134px;height:44px;line-height:44px;text-align:center;font-size:16px;color:#555;background:linear-gradient(#f7f7f7,#e6e6e6);border:1px solid #d8d8d8}
.tab.active{background:var(--blue);color:#fff;border-color:var(--blue)}
.country-panel{left:42px;top:644px;width:736px;height:633px;background:var(--panel);border:1px solid var(--line)}
.scroll-track{position:absolute;right:8px;top:2px;width:14px;height:626px;background:#f4f4f4}
.scroll-thumb{position:absolute;right:9px;top:4px;width:12px;height:315px;background:#cfcfcf;border-radius:2px}
.country-list{position:absolute;list-style:none;font-size:15px;font-weight:500;color:#333}
.country-list li{height:32.6px;display:flex;align-items:center;gap:13px}
.country-list .n{color:var(--muted);font-weight:400;margin-left:4px}
.flag{width:26px;height:17px;display:inline-block;border:1px solid rgba(0,0,0,.1)}

/* testimonials */
.testi{left:42px;top:1351px;width:736px;height:174px;background:var(--panel);border:1px solid var(--line)}
.testi-photo{position:absolute;left:25px;top:25px;width:129px;height:119px;background:linear-gradient(#f3f3f3,#e9e9e9);border:1px solid #e5e5e5}
.icon-btn{position:absolute;top:119px;width:28px;height:25px;background:var(--blue);border-radius:2px;display:flex;align-items:center;justify-content:center}
.testi-role{position:absolute;left:181px;top:38px;font-size:17px;font-weight:500;color:#333}
.testi-loc{position:absolute;left:181px;top:62px;font-size:14px;color:var(--muted)}
.testi-text{position:absolute;left:181px;top:84px;width:530px;font-size:15px;line-height:21px;color:#777}
.testi-text a{color:var(--blue)}
.dots{position:absolute;left:523px;top:42px;display:flex;gap:8px}
.dots i{width:10px;height:10px;border-radius:50%;background:#ddd;display:block}
.dots i.on{background:var(--blue)}

/* partners */
.partners{left:42px;top:1595px;width:736px;height:335px;background:var(--panel);border:1px solid var(--line)}
.partner-name{position:absolute;font-size:31px;color:#c9c9c9;font-weight:400}

/* sidebar */
.side-box{position:absolute;left:803px;width:355px;background:var(--panel);border:1px solid var(--line)}
.side-title{position:absolute;left:22px;font-family:"Roboto Condensed",sans-serif;font-weight:700;font-size:19px;color:#444;text-transform:uppercase}
.side-rule{position:absolute;left:22px;width:311px;height:1px;background:var(--line)}
.share-count{position:absolute;top:73px;width:71px;height:45px;line-height:43px;text-align:center;border:1px solid #ddd;font-size:20px;color:#333;background:#fff}
.share-btn{position:absolute;top:132px;width:71px;height:34px;line-height:34px;text-align:center;font-size:14px;color:#fff}
.share-btn.in{background:#1f6ea8}
.share-btn.mo{background:#f1f1f1;color:#d33}
.share-btn.fb{background:#3b5a9a}
.share-btn.tw{background:#2aa9e0}
.to-top{left:1138px;top:700px;width:34px;height:30px;background:#555;border-radius:2px;display:flex;align-items:center;justify-content:center}
.illus{position:absolute;inset:6px;background:linear-gradient(135deg,#f7fafc,#e4eef6 50%,#f3f6f9)}
.video{position:absolute;left:22px;top:71px;width:311px;height:168px;background:linear-gradient(#2f2f2f,#6d7074 60%,#3a3b3d)}
.video-bar{position:absolute;left:0;top:0;width:100%;height:30px;background:rgba(0,0,0,.55);color:#eee;font-size:13px;line-height:30px;padding-left:12px}
.play{position:absolute;left:135px;top:68px;width:42px;height:32px;background:rgba(0,0,0,.75);border-radius:6px;display:flex;align-items:center;justify-content:center}
.poll-opt{position:absolute;left:34px;display:flex;align-items:center;gap:14px;font-size:15px;color:#555}
.poll-opt i{width:16px;height:16px;border-radius:50%;border:1px solid #ccc;background:#f3f3f3;display:block}
.vote{position:absolute;left:22px;top:505px;width:87px;height:34px;line-height:34px;text-align:center;background:var(--blue);color:#fff;font-size:14px;border-radius:2px}
.ads-head{left:803px;top:1627px;width:355px;height:35px;line-height:35px;padding-left:11px;background:#e4e4e4;border-top:1px solid #d8d8d8;font-size:13px;font-weight:700;color:#555}
.ad{position:absolute;left:803px;width:355px;font-size:14px;line-height:20px;color:#666}
.ad b{display:block;color:#2a84c4;font-weight:700}
.ad .url{color:var(--green)}

/* success stories */
.stories{left:0;top:1975px;width:1200px;height:239px;background:#fff}
.stories-title{position:absolute;left:42px;top:27px;font-size:19px;color:#666;letter-spacing:.5px;font-weight:500}
.stories-rule{position:absolute;left:42px;top:63px;width:1116px;height:1px;background:var(--line)}
.stories-arrows{position:absolute;left:1110px;top:22px;display:flex;gap:18px}
.story{position:absolute;top:84px;width:137px;height:130px;border:1px solid #e3e3e3;padding:4px;background:#fff}
.story div{width:100%;height:100%;background:linear-gradient(160deg,#c9a48a,#e7cdb9 50%,#8a949d)}

/* footer */
.footer{left:0;top:2214px;width:1200px;height:260px;background:var(--footer)}
.footer-brand{position:absolute;left:89px;top:42px;font-size:38px;color:var(--ink)}
.footer-about{position:absolute;left:42px;top:112px;width:372px;font-size:14.5px;line-height:21px;color:#666}
.f-head{position:absolute;top:50px;font-family:"Roboto Condensed",sans-serif;font-weight:700;font-size:17px;color:#444;text-transform:uppercase}
.f-links{position:absolute;top:85px;list-style:none;font-size:15px;color:#666}
.f-links li{height:34px;display:flex;align-items:center}
.f-links li::before{content:"›";color:var(--blue);margin-right:12px;font-size:18px}
.bottom-strip{left:0;top:2474px;width:1200px;height:18px;background:#3a3a3a}
</style>
</head>
<body>

<div class="abs topbar">
  <a class="lang active" style="left:38px">En</a>
  <a class="lang" style="left:85px">Fr</a>
  <a class="lang" style="left:132px">De</a>
  <a class="lang" style="left:179px">It</a>
  <a class="util" style="left:930px">Login</a>
  <a class="util" style="left:1001px">Register</a>
  <a class="util" style="left:1088px">Bookmarks</a>
</div>

<header class="abs header">
  <div class="brand-name">Paysora</div>
  <nav class="nav">
    <a style="left:510px">Home</a>
    <a style="left:607px">Payment<span class="caret">⌄</span></a>
    <a style="left:730px">Users<span class="caret">⌄</span></a>
    <a style="left:823px">Partners</a>
    <a style="left:942px">About Us</a>
    <a style="left:1069px">Contact</a>
  </nav>
</header>
<div class="abs nav-active-bar"></div>

<section class="abs hero">
  <div class="hero-card users">
    <div class="hero-photo" role="img" aria-label="Photo of a smiling businessman in a white shirt and tie"></div>
    <div class="counter"><span>0</span><span>7</span><span>9</span><span>4</span><span>5</span></div>
    <div class="counter-label">Users</div>
    <div class="counter-rule"></div>
    <a class="hero-btn blue">Register Now</a>
  </div>
  <div class="hero-card business">
    <div class="hero-illus" role="img" aria-label="Illustration of a payment gateway with a shopping cart, verified seal, globe and computer mouse"></div>
    <a class="hero-btn red">Business</a>
  </div>
</section>

<h2 class="sec-title" style="top:545px">Countries We Support</h2>
<div class="abs tabs">
  <a class="tab" style="left:0">Map</a>
  <a class="tab" style="left:134px">Industry</a>
  <a class="tab" style="left:266px">Type</a>
  <a class="tab active" style="left:398px">Country</a>
</div>
<div class="abs country-panel">
  <ul class="country-list" style="left:46px;top:36px">
    <li><span class="flag" style="background:linear-gradient(90deg,#222 33%,#b22 33% 66%,#2a7a2a 66%)"></span>Afghanistan<span class="n">(7)</span></li>
    <li><span class="flag" style="background:#3a8a3a"></span>African Union<span class="n">(6)</span></li>
    <li><span class="flag" style="background:linear-gradient(#2a55a8 40%,#e6c020 40% 60%,#2a55a8 60%)"></span>Aland<span class="n">(2)</span></li>
    <li><span class="flag" style="background:#d2232a"></span>Albania<span class="n">(7)</span></li>
    <li><span class="flag" style="background:linear-gradient(#fff 35%,#d22 35% 65%,#fff 65%)"></span>Alderney<span class="n">(3)</span></li>
    <li><span class="flag" style="background:linear-gradient(90deg,#1a8a3a 50%,#fff 50%)"></span>Algeria<span class="n">(4)</span></li>
    <li><span class="flag" style="background:linear-gradient(#1f3a8a 45%,#fff 45% 55%,#c22 55%)"></span>American Samoa<span class="n">(3)</span></li>
    <li><span class="flag" style="background:linear-gradient(90deg,#1a3c9a 33%,#f2c400 33% 66%,#d3102a 66%)"></span>Andorra<span class="n">(5)</span></li>
    <li><span class="flag" style="background:linear-gradient(#cc1020 50%,#111 50%)"></span>Angola<span class="n">(3)</span></li>
    <li><span class="flag" style="background:#1f3a8a"></span>Anguilla<span class="n">(8)</span></li>
    <li><span class="flag" style="background:#4a7fc8"></span>Antarctica<span class="n">(3)</span></li>
    <li><span class="flag" style="background:linear-gradient(#111 40%,#2a5ab8 40% 60%,#d22 60%)"></span>Antigua &amp; Barbuda<span class="n">(6)</span></li>
    <li><span class="flag" style="background:#2a8a3a"></span>Arab League<span class="n">(3)</span></li>
    <li><span class="flag" style="background:linear-gradient(#74acdf 33%,#fff 33% 66%,#74acdf 66%)"></span>Argentina<span class="n">(2)</span></li>
    <li><span class="flag" style="background:linear-gradient(#d22 33%,#1a3ca0 33% 66%,#f2a800 66%)"></span>Armenia<span class="n">(3)</span></li>
    <li><span class="flag" style="background:linear-gradient(#4a90d0 70%,#f2d000 70% 80%,#4a90d0 80%)"></span>Aruba<span class="n">(8)</span></li>
    <li><span class="flag" style="background:#1a3c9a"></span>ASEAN<span class="n">(3)</span></li>
  </ul>
  <ul class="country-list" style="left:367px;top:36px">
    <li><span class="flag" style="background:linear-gradient(#111 30%,#fff 30% 35%,#b22 35% 65%,#fff 65% 70%,#2a7a2a 70%)"></span>Kenya<span class="n">(3)</span></li>
    <li><span class="flag" style="background:linear-gradient(#d22 55%,#2a5ab8 55%)"></span>Kiribati<span class="n">(4)</span></li>
    <li><span class="flag" style="background:#2a4aa8"></span>Kosovo<span class="n">(2)</span></li>
    <li><span class="flag" style="background:linear-gradient(#1a8a3a 33%,#fff 33% 66%,#d22 66%)"></span>Kuwait<span class="n">(6)</span></li>
    <li><span class="flag" style="background:#e0302a"></span>Kyrgyzstan<span class="n">(1)</span></li>
    <li><span class="flag" style="background:linear-gradient(#d22 25%,#1a3c9a 25% 75%,#d22 75%)"></span>Laos<span class="n">(3)</span></li>
    <li><span class="flag" style="background:linear-gradient(#9e2a33 40%,#fff 40% 60%,#9e2a33 60%)"></span>Latvia<span class="n">(4)</span></li>
    <li><span class="flag" style="background:linear-gradient(#d22 25%,#fff 25% 75%,#d22 75%)"></span>Lebanon<span class="n">(2)</span></li>
    <li><span class="flag" style="background:linear-gradient(#1a3c9a 33%,#fff 33% 66%,#1a8a3a 66%)"></span>Lesotho<span class="n">(5)</span></li>
    <li><span class="flag" style="background:repeating-linear-gradient(#c22 0 2px,#fff 2px 4px)"></span>Liberia<span class="n">(7)</span></li>
    <li><span class="flag" style="background:linear-gradient(#d22 25%,#111 25% 75%,#2a8a3a 75%)"></span>Libya<span class="n">(1)</span></li>
    <li><span class="flag" style="background:linear-gradient(#1a3c9a 50%,#d22 50%)"></span>Liechtenstein<span class="n">(6)</span></li>
    <li><span class="flag" style="background:linear-gradient(#f2c000 33%,#1a7a3a 33% 66%,#c22 66%)"></span>Lithuania<span class="n">(2)</span></li>
    <li><span class="flag" style="background:linear-gradient(#e22 33%,#fff 33% 66%,#2aa0e0 66%)"></span>Luxembourg<span class="n">(8)</span></li>
    <li><span class="flag" style="background:#2a8a5a"></span>Macao<span class="n">(5)</span></li>
    <li><span class="flag" style="background:#d2232a"></span>Macedonia<span class="n">(2)</span></li>
    <li><span class="flag" style="background:linear-gradient(90deg,#fff 33%,transparent 33%),linear-gradient(#d22 50%,#2a8a3a 50%)"></span>Madagascar<span class="n">(1)</span></li>
  </ul>
  <div class="scroll-track"></div>
  <div class="scroll-thumb"></div>
</div>

<h2 class="sec-title" style="top:1300px">Testimonials</h2>
<div class="abs testi">
  <div class="testi-photo" role="img" aria-label="Portrait of the reviewer"></div>
  <a class="icon-btn" style="left:35px">
    <svg width="13" height="13" viewBox="0 0 13 13"><circle cx="5.5" cy="5.5" r="3.8" fill="none" stroke="#fff" stroke-width="1.8"/><path d="M8.3 8.3 12 12" stroke="#fff" stroke-width="2"/></svg>
  </a>
  <a class="icon-btn" style="left:70px">
    <svg width="14" height="14" viewBox="0 0 14 14"><path d="M6 8 8 6M5 5 3 7a2 2 0 0 0 3 3l1-1M9 9l2-2a2 2 0 0 0-3-3L7 5" fill="none" stroke="#fff" stroke-width="1.7"/></svg>
  </a>
  <div class="testi-role">Front-End Developer at Nexmarket</div>
  <div class="testi-loc">Sydney, Australia</div>
  <p class="testi-text">Lorem ipsum dolor sit amet, consectetur adipisicing elit. Proin nibh augue, suscipit a, scelerisque sed, lacinia in, mi. <a>Read More</a></p>
  <div class="dots"><i></i><i></i><i></i><i></i><i></i><i></i><i class="on"></i><i></i><i></i><i></i></div>
</div>

<h2 class="sec-title" style="top:1543px">Our Partners</h2>
<div class="abs partners">
  <span class="partner-name" style="left:44px;top:34px">Lorem Ipsum</span>
  <span class="partner-name" style="left:292px;top:34px">Lorem Ipsum</span>
  <span class="partner-name" style="left:521px;top:34px">Lorem Ipsum</span>
  <span class="partner-name" style="left:44px;top:99px">Lorem Ipsum</span>
  <span class="partner-name" style="left:292px;top:99px">Lorem Ipsum</span>
  <span class="partner-name" style="left:521px;top:99px">Lorem Ipsum</span>
  <span class="partner-name" style="left:44px;top:164px">Lorem Ipsum</span>
  <span class="partner-name" style="left:292px;top:164px">Lorem Ipsum</span>
  <span class="partner-name" style="left:521px;top:164px">Lorem Ipsum</span>
  <span class="partner-name" style="left:44px;top:227px">Lorem Ipsum</span>
  <span class="partner-name" style="left:292px;top:227px">Lorem Ipsum</span>
  <span class="partner-name" style="left:521px;top:227px">Lorem Ipsum</span>
</div>

<aside>
  <div class="side-box" style="top:529px;height:187px">
    <div class="side-title" style="top:17px">Share us with your friends</div>
    <div class="side-rule" style="top:50px"></div>
    <div class="share-count" style="left:23px">500</div>
    <div class="share-count" style="left:102px">2.7K</div>
    <div class="share-count" style="left:182px">1.3K</div>
    <div class="share-count" style="left:261px">868</div>
    <a class="share-btn in" style="left:23px">Linkora</a>
    <a class="share-btn mo" style="left:102px">Moravu</a>
    <a class="share-btn fb" style="left:182px">Friendloop</a>
    <a class="share-btn tw" style="left:261px">Chirpa</a>
  </div>
  <a class="abs to-top"><svg width="16" height="10" viewBox="0 0 16 10"><path d="M2 8 8 2l6 6" fill="none" stroke="#fff" stroke-width="2.4"/></svg></a>

  <div class="side-box" style="top:741px;height:283px">
    <div class="illus" role="img" aria-label="Diagram of payment channels around a central terminal: electronic money, mobile commerce, phones, e-invoicing, terminals and plastic cards"></div>
  </div>

  <div class="side-box" style="top:1041px;height:562px">
    <div class="side-title" style="top:17px">Support Video: How to use</div>
    <div class="side-rule" style="top:50px"></div>
    <div class="video" role="img" aria-label="Video still of a person walking at dusk">
      <div class="video-bar">Careers Introduction</div>
      <div class="play"><svg width="14" height="16" viewBox="0 0 14 16"><path d="M2 1l11 7-11 7z" fill="#fff"/></svg></div>
    </div>
    <div class="side-title" style="top:268px">The Poll</div>
    <div class="side-rule" style="top:300px"></div>
    <label class="poll-opt" style="top:327px"><i></i>Definitely Yes</label>
    <label class="poll-opt" style="top:360px"><i></i>Rather Yes</label>
    <label class="poll-opt" style="top:393px"><i></i>I'm Not Sure</label>
    <label class="poll-opt" style="top:426px"><i></i>Rather Not</label>
    <label class="poll-opt" style="top:459px"><i></i>No Way!</label>
    <a class="vote">Vote Now</a>
  </div>

  <div class="abs ads-head">Ads by Adquill</div>
  <div class="ad" style="top:1677px"><b>Find Your Dream Job With Career</b>Proin nibh augue, suscipit a, scelerisque sed, lacinia in, mi. Cras vel lorem. Etiam pellentesque aliquet tellus.<br><span class="url">example.com</span></div>
  <div class="ad" style="top:1796px"><b>Find Your Dream Job With Career</b>Proin nibh augue, suscipit a, scelerisque sed, lacinia in, mi. Cras vel lorem. Etiam pellentesque aliquet tellus.<br><span class="url">example.com</span></div>
</aside>

<section class="abs stories">
  <div class="stories-title">SUCCESS STORIES</div>
  <div class="stories-arrows">
    <svg width="12" height="18" viewBox="0 0 12 18"><path d="M9 2 3 9l6 7" fill="none" stroke="#bbb" stroke-width="2"/></svg>
    <svg width="12" height="18" viewBox="0 0 12 18"><path d="M3 2l6 7-6 7" fill="none" stroke="#bbb" stroke-width="2"/></svg>
  </div>
  <div class="stories-rule"></div>
  <div class="story" style="left:42px"><div role="img" aria-label="Customer portrait"></div></div>
  <div class="story" style="left:205px"><div role="img" aria-label="Customer portrait"></div></div>
  <div class="story" style="left:367px"><div role="img" aria-label="Customer portrait"></div></div>
  <div class="story" style="left:530px"><div role="img" aria-label="Customer portrait"></div></div>
  <div class="story" style="left:692px"><div role="img" aria-label="Customer portrait"></div></div>
  <div class="story" style="left:854px"><div role="img" aria-label="Customer portrait"></div></div>
  <div class="story" style="left:1016px"><div role="img" aria-label="Customer portrait"></div></div>
</section>

<footer class="abs footer">
  <div class="footer-brand">Paysora</div>
  <p class="footer-about">Lorem ipsum dolor sit amet, consectetur adipisicing elit. Proin nibh augue, suscipit a, scelerisque sed, lacinia in, mi. Praesent sodales velit quis augue. Cras suscipit.</p>
  <div class="f-head" style="left:433px">Navigation</div>
  <ul class="f-links" style="left:433px"><li>Home</li><li>Jobs</li><li>Partners</li><li>About Us</li></ul>
  <ul class="f-links" style="left:587px"><li>Contact Us</li><li>Terms &amp; Conditions</li><li>Privacy Policy</li></ul>
  <div class="f-head" style="left:815px">Follow Us</div>
  <ul class="f-links" style="left:815px"><li>Blog</li><li>Chirpa</li><li>Friendloop</li><li>Vidlane</li></ul>
  <div class="f-head" style="left:981px">Popular Jobs</div>
  <ul class="f-links" style="left:981px"><li>Web Developer</li><li>Web Designer</li><li>UX Engineer</li><li>Account Manager</li></ul>
</footer>
<div class="abs bottom-strip"></div>

</body>
</html>
```